Tavlor Suite Background image creation.

We need someone to develop an image that is 1920x1080 using our company logo and and colors. We will be using this as the login page background on tavlorsuite.net for all our clients.

```html
<!DOCTYPE html>
<html lang="en">
<head>
<meta charset="UTF-8">
<title>Harborline Systems – Sign in</title>
<link href="https://fonts.googleapis.com/css2?family=Roboto:wght@400;500&display=swap" rel="stylesheet">
<style>
  :root {
    --sky-top: #36a7d6;
    --sky-mid: #2ea2dc;
    --sky-deep: #1e94e6;
    --glow: #16e0f0;
    --brand-cyan: #00c8f8;
    --white: #ffffff;
    --field-icon: #b3b3b3;
    --field-text: #8a8a8a;
    --button: #00c4f5;
  }
  * { box-sizing: border-box; margin: 0; padding: 0; }
  html, body { width: 1200px; height: 675px; overflow: hidden; }
  body {
    position: relative;
    font-family: "Roboto", sans-serif;
    background: var(--sky-top);
  }
  .backdrop {
    position: absolute; inset: 0;
    background:
      radial-gradient(ellipse 60% 45% at 55% 105%, rgba(22,224,240,0.85) 0%, rgba(22,224,240,0.35) 45%, rgba(22,224,240,0) 75%),
      linear-gradient(180deg, var(--sky-top) 0%, var(--sky-top) 40%, var(--sky-mid) 65%, var(--sky-deep) 100%);
  }
  .brand {
    position: absolute;
    left: 442px; top: 100px;
    display: flex; align-items: center; gap: 18px;
  }
  .brand-mark {
    width: 74px; height: 74px; border-radius: 50%;
    background: var(--brand-cyan);
  }
  .brand-name {
    font-weight: 500;
    font-size: 36px;
    color: var(--brand-cyan);
    letter-spacing: 0.5px;
  }
  .login-panel {
    position: absolute;
    left: 442px; top: 258px;
    width: 316px; height: 280px;
    border: 1px solid rgba(255,255,255,0.9);
    border-radius: 6px;
  }
  .field {
    position: absolute; left: 12px;
    width: 289px; height: 42px;
    background: var(--white);
    border-radius: 4px;
    box-shadow: 0 2px 4px rgba(0,0,0,0.12);
    display: flex; align-items: center;
    padding-left: 20px;
    color: var(--field-text);
    font-size: 12.5px;
  }
  .field svg { width: 18px; height: 18px; margin-right: 16px; fill: var(--field-icon); }
  .field-username { top: 82px; }
  .field-password { top: 139px; letter-spacing: 1px; font-size: 11px; }
  .login-button {
    position: absolute; left: 12px; top: 194px;
    width: 289px; height: 31px;
    background: var(--button);
    color: var(--white);
    font-size: 12px;
    display: flex; align-items: center; justify-content: center;
    box-shadow: 0 2px 3px rgba(0,0,0,0.12);
  }
  .panel-footer {
    position: absolute; left: 21px; right: 26px; top: 240px;
    display: flex; justify-content: space-between; align-items: center;
    color: var(--white); font-size: 12px;
  }
  .remember { display: flex; align-items: center; gap: 6px; }
  .remember .box { width: 13px; height: 13px; background: var(--white); border-radius: 1px; }
  .copyright {
    position: absolute; top: 547px; left: 0; width: 1192px;
    text-align: center; color: var(--white); font-size: 11px;
  }
</style>
</head>
<body>
  <div class="backdrop" role="img" aria-label="Soft blue background with concentric rings and glowing bokeh dots"></div>

  <div class="brand">
    <div class="brand-mark"></div>
    <span class="brand-name">Harborline Systems</span>
  </div>

  <div class="login-panel">
    <div class="field field-username">
      <svg viewBox="0 0 24 24" aria-hidden="true"><circle cx="12" cy="7" r="5"/><path d="M2 23c0-6 4.5-9 10-9s10 3 10 9z"/></svg>
      Username
    </div>
    <div class="field field-password">
      <svg viewBox="0 0 24 24" aria-hidden="true"><path d="M7 10V7a5 5 0 0 1 10 0v3h-2V7a3 3 0 0 0-6 0v3z"/><rect x="4" y="10" width="16" height="13" rx="1"/></svg>
      ********
    </div>
    <div class="login-button">LOGIN</div>
    <div class="panel-footer">
      <span class="remember"><span class="box"></span>Remember me</span>
      <span class="forgot">Forgot Password ?</span>
    </div>
  </div>

  <p class="copyright">Copyright 2018</p>
</body>
</html>
```